依頼詳細
会社案内なので、金額などは入れる必要はないです。
この案内をみて、新規の企業が、弊社に依頼したくなるような内容にしてもらえると助かります。
一般廃棄物収集運搬許可がないと不用品回収や遺品整理の仕事をすることが出来ないのですが、それを知らないお客様が多いので、それを理解していただければと思います。
記載項目
似顔絵は必ず入れてください。
ワードで掲載してほしい内容は添付しています。
チラシやホームページもぜひ参考にしてほしいです。
生活まもり団ホームページ
https://mamoridan-life.jp/
専門家まもり団ホームページ
https://mamoridan-pro.jp/

建材事業
https://r-hazuki.jp/
サイズ
A4
ページ数
両面
希望イメージ
シンプル 複雑
単色 カラフル
暗い 明るい
日常 高級
遊び心 厳粛
未来的 伝統的
女性的 男性的
希望する色
青系、水色系
納品ファイル
• 高解像度JPG (.jpg)
• イラストレーター形式 (.ai)
• PNG形式 (.png)
補足説明

とてもシンプルかつ分かりやすい仕上がりだったのが気に入りました。

沢山の方が提案していただき、本当にありがとうございました。
ぜひまたお願いすることもあるかと思いますので、その時は宜しくお願いいたします。

```html
<!DOCTYPE html>
<html lang="ja">
<head>
<meta charset="utf-8">
<title>株式会社ハヅキ まもり団事業部 会社案内</title>
<link rel="stylesheet" href="https://fonts.googleapis.com/css2?family=Noto+Sans+JP:wght@400;500;700;900&display=swap">
<style>
  :root {
    --blue: #1f6dbf;
    --blue-deep: #17589e;
    --blue-light: #2f8fd6;
    --blue-pale: #d6eaf8;
    --white: #ffffff;
    --ink: #2b2b2b;
  }
  * { margin: 0; padding: 0; box-sizing: border-box; }
  html, body { width: 846px; height: 1200px; overflow: hidden; background: var(--white); }
  body { font-family: "Noto Sans JP", sans-serif; color: var(--blue); }
  .page { position: relative; width: 846px; height: 1200px; overflow: hidden; background: var(--white); }
  .backdrop { position: absolute; inset: 0; }

  .heading { position: absolute; left: 30px; top: 14px; }
  .heading__company { font-size: 22px; font-weight: 700; letter-spacing: .04em; }
  .heading__division { font-size: 40px; font-weight: 900; line-height: 1.2; letter-spacing: .02em; }
  .heading__title { font-size: 40px; font-weight: 900; line-height: 1.2; letter-spacing: .28em; }

  .intro { position: absolute; left: 30px; top: 150px; width: 225px; padding-left: 10px;
    border-left: 3px solid var(--blue); font-size: 11px; line-height: 1.75; font-weight: 500; color: var(--blue-light); }

  .tile { position: absolute; transform: translate(-50%, -50%); text-align: center;
    font-weight: 700; line-height: 1.35; }
  .tile--sm { font-size: 15px; width: 118px; }
  .tile--lg { font-size: 25px; width: 120px; line-height: 1.3; }
  .tile--on-blue { color: var(--white); }
  .tile--service { width: 96px; }
  .tile__note { display: block; font-size: 8px; font-weight: 500; line-height: 1.35; margin-bottom: 3px; color: var(--ink); }
  .tile__name { display: block; font-size: 17px; font-weight: 900; line-height: 1.3; color: var(--blue); }
  .tile__name--pro { color: var(--blue-deep); }

  .invite { position: absolute; left: 690px; top: 668px; transform: translate(-50%, -50%);
    width: 230px; text-align: center; font-size: 25px; font-weight: 900; line-height: 1.5; color: var(--blue); }

  .qualify { position: absolute; left: 712px; top: 908px; width: 128px; text-align: center; color: var(--ink); }
  .qualify__title { font-size: 16px; font-weight: 900; color: var(--blue); margin-bottom: 6px; }
  .qualify__list { list-style: none; font-size: 13px; font-weight: 700; line-height: 1.3; }
  .qualify__list li { margin-bottom: 6px; }

  .brand { position: absolute; left: 40px; top: 1110px; display: flex; align-items: center; gap: 8px; }
  .brand__mark { width: 26px; height: 26px; border-radius: 50%; background: var(--blue); }
  .brand__name { font-size: 18px; font-weight: 700; color: var(--blue); }
  .company { position: absolute; right: 30px; top: 1152px; font-size: 26px; font-weight: 900; color: var(--blue); letter-spacing: .03em; }
</style>
</head>
<body>
<main class="page">
  <svg class="backdrop" width="846" height="1200" viewBox="0 0 846 1200" xmlns="http://www.w3.org/2000/svg">
    <defs>
      <linearGradient id="photoTone" x1="0" y1="0" x2="0" y2="1">
        <stop offset="0" stop-color="#3d84c9"/>
        <stop offset="0.42" stop-color="#7fb3db"/>
        <stop offset="0.55" stop-color="#8fb46a"/>
        <stop offset="0.8" stop-color="#4f7f34"/>
        <stop offset="1" stop-color="#2d5a23"/>
      </linearGradient>
      <pattern id="lattice" patternUnits="userSpaceOnUse" x="420" y="410" width="170" height="160">
        <path d="M85 0 L170 80 L85 160 L0 80 Z" fill="none" stroke="#ffffff" stroke-width="8"/>
      </pattern>
      <clipPath id="mosaicArea">
        <polygon points="500,0 846,0 846,1098 0,1098 0,620 250,410 420,250 420,0"/>
      </clipPath>
    </defs>

    <g clip-path="url(#mosaicArea)">
      <rect x="0" y="0" width="846" height="1100" fill="url(#photoTone)" role="img" aria-label="重ねた手、木の人形、森の緑と若葉の写真"/>
      <polygon points="760,170 845,250 760,330 675,250" fill="var(--blue-deep)"/>
      <polygon points="590,170 675,250 590,330 505,250" fill="var(--blue)"/>
      <polygon points="250,490 335,570 250,650 165,570" fill="var(--blue)"/>
      <polygon points="760,330 845,410 760,490 675,410" fill="var(--blue-light)"/>
      <rect x="0" y="0" width="846" height="1100" fill="url(#lattice)"/>
    </g>

    <!-- service tiles -->
    <polygon points="600,8 680,88 600,168 520,88" fill="var(--white)"/>
    <polygon points="760,8 840,88 760,168 680,88" fill="var(--white)"/>

    <!-- feature tiles -->
    <polygon points="505,254 585,330 505,406 425,330" fill="var(--blue-pale)"/>
    <polygon points="420,334 500,410 420,486 340,410" fill="var(--white)"/>
    <polygon points="590,334 670,410 590,486 510,410" fill="var(--white)"/>
    <polygon points="335,414 415,490 335,566 255,490" fill="var(--white)"/>
    <polygon points="505,414 585,490 505,566 425,490" fill="var(--blue)"/>
    <polygon points="670,414 750,490 670,566 590,490" fill="var(--blue)"/>
    <polygon points="420,494 500,570 420,646 340,570" fill="var(--white)"/>
    <polygon points="590,494 670,570 590,646 510,570" fill="var(--white)"/>

    <!-- invitation tile -->
    <polygon points="690,540 846,680 690,830 540,680" fill="var(--white)"/>
    <circle cx="692" cy="772" r="34" fill="#c9b59a" role="img" aria-label="担当者の似顔絵イラスト"/>

    <!-- qualification panel -->
    <rect x="704" y="890" width="142" height="208" fill="var(--white)" opacity="0.93"/>

    <!-- footer illustration -->
    <rect x="550" y="1104" width="180" height="44" rx="6" fill="#a9c7e4" role="img" aria-label="スタッフとトラックのイラスト"/>
  </svg>

  <header class="heading">
    <p class="heading__company">株式会社ハヅキ</p>
    <h1 class="heading__division">まもり団事業部</h1>
    <p class="heading__title">会社案内</p>
  </header>

  <p class="intro">多くの地域住民の方々に支えられて、仕事を続けることが出来ました。この地域の暮らしを守る存在として「まもり団事業部」としてスタートしました。皆さまのお困りごとに寄り添い、地域の安心をお届けします。</p>

  <div class="tile tile--service" style="left:600px;top:92px;">
    <span class="tile__note">一般の方の<br>お困りごとを<br>解決する</span>
    <span class="tile__name">生活<br>まもり団</span>
  </div>
  <div class="tile tile--service" style="left:760px;top:92px;">
    <span class="tile__note">弁護士や<br>司法書士などを<br>サポート</span>
    <span class="tile__name tile__name--pro">専門家<br>まもり団</span>
  </div>

  <p class="tile tile--sm" style="left:505px;top:330px;">お見積もり<br>無料</p>
  <p class="tile tile--sm" style="left:420px;top:410px;">地元生まれの<br>企業</p>
  <p class="tile tile--sm" style="left:590px;top:410px;">損害保険<br>加入済み</p>
  <p class="tile tile--sm" style="left:335px;top:490px;">一般廃棄物<br>収集運搬<br>許可業者</p>
  <p class="tile tile--sm tile--on-blue" style="left:505px;top:490px;">湊和県<br>士業協同組合<br>特約店</p>
  <p class="tile tile--sm tile--on-blue" style="left:670px;top:490px;">費用の<br>支払いサイト<br>相談可能</p>
  <p class="tile tile--lg" style="left:420px;top:570px;">不用品<br>回収</p>
  <p class="tile tile--lg" style="left:590px;top:570px;">遺品<br>整理</p>

  <p class="invite">まずはお気軽に<br>ご相談ください！</p>

  <section class="qualify">
    <h2 class="qualify__title">資格保有者</h2>
    <ul class="qualify__list">
      <li>遺品整理士</li>
      <li>相続診断士</li>
      <li>生前整理<br>アドバイザー2級</li>
      <li>2級土木施工<br>管理技士</li>
    </ul>
  </section>

  <footer>
    <div class="brand"><span class="brand__mark"></span><span class="brand__name">生活まもり団</span></div>
    <p class="company">株式会社ハヅキ</p>
  </footer>
</main>
</body>
</html>
```